Granite Valve Works - Single page line card revamp - new business rebrand

hello,

Our company, KLB (www.klb-harwell.example), just purchased a business, Granite Valve Works (GVW), and we want to revamp their line card to be more modern and use a color scheme similar to KLB's branding. I have attached the existing line card and the GVW logo for the submittal. Please also include their phone number on the brochure: 555-014-7290
I also included a flyer from KLB, as it would also be nice to incorporate the Kinetic Lift & Bearings (KLB) brand into the flyer.

Thanks
Noel

```html
<!DOCTYPE html>
<html lang="en">
<head>
<meta charset="utf-8">
<title>Granite Valve Works – Line Card</title>
<link rel="stylesheet" href="https://fonts.googleapis.com/css2?family=Montserrat:wght@700;800;900&family=Poppins:wght@400;500;600;700&display=swap">
<style>
  :root{
    --ink:#0a0a0a;
    --navy:#123f86;
    --royal:#1a56ab;
    --sky:#2b8bd2;
    --white:#ffffff;
    --rule:#c9c9c9;
    --heading-blue:#1a4fa3;
  }
  *{margin:0;padding:0;box-sizing:border-box}
  html,body{width:903px;height:1200px;overflow:hidden;background:#fff}
  body{font-family:'Poppins',sans-serif;color:var(--ink)}
  .card{position:relative;width:903px;height:1200px;background:var(--white);overflow:hidden}
  .layer{position:absolute;left:0;top:0}
  .abs{position:absolute}

  .eyebrow{left:64px;top:60px;font-family:'Montserrat',sans-serif;font-weight:900;font-size:19px;letter-spacing:7px;color:var(--white)}
  .pills{left:64px;top:97px;display:flex;height:28px}
  .pill{display:flex;align-items:center;justify-content:center;height:28px;border-radius:14px;
        background:linear-gradient(90deg,var(--royal),var(--sky));color:var(--white);
        font-family:'Montserrat',sans-serif;font-weight:800;font-size:15px;margin-right:-4px;box-shadow:-3px 0 4px rgba(0,0,0,.35)}
  .pill.prompt{width:118px}
  .pill.quality{width:182px}
  .pill.service{width:124px}
  .headline{left:64px;top:134px;font-family:'Montserrat',sans-serif;font-weight:900;font-size:49px;line-height:45px;color:var(--white)}
  .lede{left:64px;top:285px;border-left:4px solid var(--sky);padding-left:10px;color:var(--white);font-size:17.5px;line-height:23px}

  .section-title{left:66px;font-family:'Montserrat',sans-serif;font-weight:800;font-size:20px;line-height:22px;color:var(--ink);white-space:nowrap}
  .section-title span{color:var(--heading-blue);display:block}
  .brand-grid{left:64px;display:grid}
  .brand{height:36px;border:1px solid #555;border-radius:3px;display:flex;align-items:center;justify-content:center;
         font-weight:600;font-size:10.5px;color:var(--heading-blue);text-align:center;gap:4px;white-space:nowrap}
  .brand .dot{width:8px;height:8px;border-radius:50%;background:var(--heading-blue)}
  .divider{left:64px;top:652px;width:327px;height:1px;background:var(--rule)}

  .panel-title{left:469px;font-family:'Montserrat',sans-serif;font-weight:800;font-size:19px;line-height:22px;color:var(--white);white-space:nowrap}
  .ticks{left:469px;list-style:none;color:var(--white);font-size:13.6px}
  .ticks li{display:flex;align-items:center;height:25.6px}
  .ticks svg{margin-right:9px}
  .panel-rule{left:469px;top:700px;width:347px;height:1px;background:rgba(255,255,255,.6)}
  .members{left:469px;top:884px;width:330px;color:var(--white)}
  .members h3{font-family:'Montserrat',sans-serif;font-weight:800;font-size:12.5px;line-height:14.5px}
  .members p{font-size:12.5px;line-height:15.5px;margin-top:2px}

  .mark{left:68px;top:1000px;display:flex;align-items:center;gap:8px;font-family:'Montserrat',sans-serif;font-weight:900;font-size:46px;line-height:50px;color:var(--royal)}
  .mark .sq{width:18px;height:18px;background:var(--royal)}
  .division{left:68px;top:1056px;width:160px;font-family:'Montserrat',sans-serif;font-weight:800;font-size:9.5px;line-height:12px;letter-spacing:.6px;color:var(--ink)}
  .company{left:248px;top:1033px;display:flex;align-items:center;width:600px;font-family:'Montserrat',sans-serif;font-weight:800;font-size:19px;white-space:nowrap}
  .company span{color:var(--heading-blue);margin-left:6px}
  .company i{flex:1;height:1px;background:var(--rule);margin-left:10px}
  .contacts{left:248px;top:1075px;display:flex;font-size:12.3px;font-weight:500;line-height:17px}
  .contact{display:flex;flex-direction:column;gap:2px;padding-right:11px;margin-right:11px;border-right:1px solid #999;min-height:36px}
  .contact:last-child{border:none;margin:0;padding:0}
  .contact-line{display:flex;align-items:flex-start;gap:6px;white-space:nowrap}
  .ico{width:16px;height:16px;border-radius:50%;background:var(--royal);flex:none;display:flex;align-items:center;justify-content:center;margin-top:1px}
</style>
</head>
<body>
<div class="card">

  <svg class="layer" width="903" height="1200" viewBox="0 0 903 1200" aria-hidden="true">
    <defs>
      <linearGradient id="panelFill" x1="0" y1="0" x2="0" y2="1">
        <stop offset="0" stop-color="#1a4fa0"/>
        <stop offset="1" stop-color="#2a8ad0"/>
      </linearGradient>
      <linearGradient id="swoosh" x1="0" y1="0" x2="1" y2="0">
        <stop offset="0" stop-color="#123f86"/>
        <stop offset="1" stop-color="#2b8bd2"/>
      </linearGradient>
    </defs>
    <path d="M438 454 C600 430 740 390 835 315 V1002 H498 Q438 1002 438 942 Z" fill="url(#panelFill)"/>
    <path d="M438 864 H835 V1002 H498 Q438 1002 438 942 Z" fill="var(--navy)"/>
    <path d="M100 392 C260 450 430 455 580 438 C730 420 840 320 903 226 V262 C840 350 730 432 580 448 C420 462 250 450 100 392 Z" fill="url(#swoosh)"/>
    <path d="M0 0 H903 V204 C800 330 620 418 400 418 C240 418 110 385 0 334 Z" fill="var(--ink)"/>
  </svg>

  <svg class="layer" width="903" height="420" viewBox="0 0 903 420" role="img" aria-label="Photo: technician in safety glasses grinding metal with bright sparks">
    <defs>
      <linearGradient id="photoTone" x1="0" y1="0" x2="1" y2="1">
        <stop offset="0" stop-color="#0d1f3d"/>
        <stop offset=".55" stop-color="#3b3026"/>
        <stop offset="1" stop-color="#a8763e"/>
      </linearGradient>
    </defs>
    <path d="M500 0 H903 V204 C840 290 760 340 690 372 L500 382 Z" fill="url(#photoTone)"/>
  </svg>

  <div class="abs eyebrow">WE PROVIDE</div>
  <div class="abs pills">
    <div class="pill prompt">PROMPT</div>
    <div class="pill quality">QUALITY SALES</div>
    <div class="pill service">SERVICE</div>
  </div>
  <div class="abs headline">OF NEW AND<br>USED ELECTRIC<br>MOTORS</div>
  <div class="abs lede">We maintain large inventories in order<br>to betterservice our valued customers.</div>

  <div class="abs section-title" style="top:478px">NEW MOTOR SALES FOR<span>THESE BRANDS AND MORE</span></div>
  <div class="abs brand-grid" style="top:537px;grid-template-columns:repeat(4,74px);column-gap:7px">
    <div class="brand">Arlen Drive</div>
    <div class="brand">Corvo</div>
    <div class="brand">Halvet</div>
    <div class="brand">Tarrow</div>
  </div>
  <div class="abs brand-grid" style="top:583px;grid-template-columns:repeat(3,101px);column-gap:8px">
    <div class="brand"><i class="dot"></i>Brightpole</div>
    <div class="brand">Stridewell</div>
    <div class="brand">Orbis Electric</div>
  </div>
  <div class="abs divider"></div>

  <div class="abs section-title" style="top:680px">WE ALSO PROVIDE NEW<span>PROCESS EQUIPMENT FOR</span><span>THESE BRNDS AND MORE</span></div>
  <div class="abs brand-grid" style="top:761px;grid-template-columns:repeat(3,101px);gap:11px 9px">
    <div class="brand">Fenmark</div>
    <div class="brand">Dosaline</div>
    <div class="brand">Aerith Blower</div>
    <div class="brand">Harlow Pumps</div>
    <div class="brand">Pistora</div>
    <div class="brand">Keeler</div>
    <div class="brand">Vantage Pump</div>
    <div class="brand">Ridgeline Pump</div>
    <div class="brand">Oshiro</div>
    <div class="brand">Nordflo</div>
    <div class="brand">Tidal Flow</div>
  </div>

  <div class="abs panel-title" style="top:480px">OUR SERVICES INCLUDE</div>
  <ul class="abs ticks" style="top:509px">
    <li><svg width="10" height="10" viewBox="0 0 10 10"><circle cx="5" cy="5" r="5" fill="#fff"/><path d="M2.6 5.2 4.3 6.8 7.4 3.5" stroke="#1a56ab" stroke-width="1.5" fill="none"/></svg>Electric motor repairing</li>
    <li><svg width="10" height="10" viewBox="0 0 10 10"><circle cx="5" cy="5" r="5" fill="#fff"/><path d="M2.6 5.2 4.3 6.8 7.4 3.5" stroke="#1a56ab" stroke-width="1.5" fill="none"/></svg>Pd &amp; centigaul blower repair</li>
    <li><svg width="10" height="10" viewBox="0 0 10 10"><circle cx="5" cy="5" r="5" fill="#fff"/><path d="M2.6 5.2 4.3 6.8 7.4 3.5" stroke="#1a56ab" stroke-width="1.5" fill="none"/></svg>Hydraulic repair</li>
    <li><svg width="10" height="10" viewBox="0 0 10 10"><circle cx="5" cy="5" r="5" fill="#fff"/><path d="M2.6 5.2 4.3 6.8 7.4 3.5" stroke="#1a56ab" stroke-width="1.5" fill="none"/></svg>Process pump repair</li>
    <li><svg width="10" height="10" viewBox="0 0 10 10"><circle cx="5" cy="5" r="5" fill="#fff"/><path d="M2.6 5.2 4.3 6.8 7.4 3.5" stroke="#1a56ab" stroke-width="1.5" fill="none"/></svg>Vertical turbine pump repair</li>
    <li><svg width="10" height="10" viewBox="0 0 10 10"><circle cx="5" cy="5" r="5" fill="#fff"/><path d="M2.6 5.2 4.3 6.8 7.4 3.5" stroke="#1a56ab" stroke-width="1.5" fill="none"/></svg>Laser alignments</li>
    <li><svg width="10" height="10" viewBox="0 0 10 10"><circle cx="5" cy="5" r="5" fill="#fff"/><path d="M2.6 5.2 4.3 6.8 7.4 3.5" stroke="#1a56ab" stroke-width="1.5" fill="none"/></svg>Vibration analysis</li>
  </ul>
  <div class="abs panel-rule"></div>
  <div class="abs panel-title" style="top:712px">ADDITIONAL SERRVICES OFFERED</div>
  <ul class="abs ticks" style="top:746px">
    <li><svg width="10" height="10" viewBox="0 0 10 10"><circle cx="5" cy="5" r="5" fill="#fff"/><path d="M2.6 5.2 4.3 6.8 7.4 3.5" stroke="#1f6fbe" stroke-width="1.5" fill="none"/></svg>Control Panel Design</li>
    <li><svg width="10" height="10" viewBox="0 0 10 10"><circle cx="5" cy="5" r="5" fill="#fff"/><path d="M2.6 5.2 4.3 6.8 7.4 3.5" stroke="#1f6fbe" stroke-width="1.5" fill="none"/></svg>Automation Scada Support</li>
    <li><svg width="10" height="10" viewBox="0 0 10 10"><circle cx="5" cy="5" r="5" fill="#fff"/><path d="M2.6 5.2 4.3 6.8 7.4 3.5" stroke="#1f6fbe" stroke-width="1.5" fill="none"/></svg>Roots Type Blower Packages</li>
    <li><svg width="10" height="10" viewBox="0 0 10 10"><circle cx="5" cy="5" r="5" fill="#fff"/><path d="M2.6 5.2 4.3 6.8 7.4 3.5" stroke="#1f6fbe" stroke-width="1.5" fill="none"/></svg>Booster Skid Fabrication</li>
  </ul>
  <div class="abs members">
    <h3>WE ARE PROUD MEMBERS OF AMRA AND<br>ADHERE TO THEIR HIGH STANDARDS</h3>
    <p>Our competent staff is available 24 hours a day<br>to assist you with your needs for motors, pumps<br>and related equipmen</p>
  </div>

  <div class="abs mark"><i class="sq"></i>GVW</div>
  <div class="abs division">A DIVISION OF KLB<br>KINETIC LIFT &amp; BEARINGS</div>
  <div class="abs company">GRANITE<span>VALVE WORKS</span><i></i></div>
  <div class="abs contacts">
    <div class="contact">
      <div class="contact-line">
        <span class="ico"><svg width="8" height="10" viewBox="0 0 8 10"><path d="M4 0a3.5 3.5 0 0 0-3.5 3.5C.5 6 4 10 4 10s3.5-4 3.5-6.5A3.5 3.5 0 0 0 4 0z" fill="#fff"/><circle cx="4" cy="3.5" r="1.3" fill="#1a56ab"/></svg></span>
        <span>58 Millrace Lane<br>Harwell, VA 24000</span>
      </div>
    </div>
    <div class="contact">
      <div class="contact-line">
        <span class="ico"><svg width="9" height="7" viewBox="0 0 9 7"><rect x=".5" y=".5" width="8" height="6" fill="none" stroke="#fff"/><path d="M.5 .5 4.5 4 8.5 .5" stroke="#fff" fill="none"/></svg></span>
        <span>service@gvw-klb.example</span>
      </div>
      <div class="contact-line">
        <span class="ico"><svg width="9" height="9" viewBox="0 0 9 9"><path d="M2 .5 3.5 2.6 2.6 3.6C3.2 5 4 5.8 5.4 6.4L6.4 5.5 8.5 7 7.6 8.5C4 8.3.7 5 .5 1.4Z" fill="#fff"/></svg></span>
        <span>555-014-7290</span>
      </div>
    </div>
    <div class="contact">
      <div class="contact-line">
        <span class="ico"><svg width="10" height="10" viewBox="0 0 10 10"><circle cx="5" cy="5" r="4" fill="none" stroke="#fff"/><path d="M1 5h8M5 1c-2 2.5-2 5.5 0 8M5 1c2 2.5 2 5.5 0 8" stroke="#fff" fill="none" stroke-width=".8"/></svg></span>
        <span>www.klb-harwell.example</span>
      </div>
    </div>
  </div>

</div>
</body>
</html>
```